School Poster

Design so that these can be placed in classrooms across the school.

Attached is another design we have had done. Use a similar theme.

Consider using themes from https://calderwoodhs.lumorin.edu/

please edit Binder1 doc.

Target Market(s)

Students and teachers

```html
<!DOCTYPE html>
<html lang="en">
<head>
<meta charset="utf-8">
<title>Before You Ask the Teacher – Calderwood High School</title>
<link href="https://fonts.googleapis.com/css2?family=Bebas+Neue&family=Barlow+Condensed:wght@500;600;700&display=swap" rel="stylesheet">
<style>
  :root {
    --navy: #1f3566;
    --navy-deep: #1c4584;
    --blue: #1b4589;
    --yellow: #f9e06b;
    --white: #ffffff;
    --ink: #222222;
    --placeholder: #2c5596;
  }
  * { margin: 0; padding: 0; box-sizing: border-box; }
  html, body { width: 849px; height: 1200px; overflow: hidden; }
  body {
    position: relative;
    background: linear-gradient(180deg, var(--navy) 0%, var(--navy-deep) 60%);
    font-family: "Barlow Condensed", sans-serif;
    color: var(--blue);
  }
  .backdrop { position: absolute; left: 0; top: 0; width: 849px; height: 1200px; }

  .school-name {
    position: absolute; left: 42px; top: 70px; width: 180px;
    text-align: center;
    font-family: "Bebas Neue", sans-serif;
    color: var(--white); font-size: 38px; line-height: 38px;
  }
  .school-name .dot {
    display: block; width: 46px; height: 46px; margin: 0 auto 12px;
    border-radius: 50%; background: var(--yellow);
  }

  .title {
    position: absolute; left: 262px; top: 30px;
    font-family: "Bebas Neue", sans-serif; font-weight: 400;
    color: var(--white); font-size: 92px; line-height: 83px; letter-spacing: 0.5px;
  }
  .subtitle {
    position: absolute; left: 264px; top: 208px;
    font-family: "Bebas Neue", sans-serif;
    color: var(--yellow); font-size: 63px; line-height: 60px; letter-spacing: 0.5px;
  }

  .step { position: absolute; top: 320px; width: 213px; height: 640px; }
  .step-1 { left: 57px; }
  .step-2 { left: 319px; }
  .step-3 { left: 584px; }

  .step-frame {
    position: absolute; left: 0; top: 0; width: 213px; height: 160px;
    border: 3px solid var(--yellow); border-bottom: none;
    border-radius: 10px 10px 0 0;
  }
  .step-number {
    position: absolute; left: -33px; top: -17px; width: 70px; height: 70px;
    border-radius: 50%; background: var(--navy);
    display: flex; align-items: center; justify-content: center;
  }
  .step-number span {
    width: 50px; height: 50px; border-radius: 50%; background: var(--white);
    color: var(--navy); font-family: "Bebas Neue", sans-serif; font-size: 40px;
    display: flex; align-items: center; justify-content: center; padding-top: 3px;
  }
  .step-icon {
    position: absolute; left: 52px; top: 24px; width: 110px; height: 112px;
    background: var(--placeholder); border-radius: 10px;
  }
  .step-label {
    position: absolute; left: -2px; top: 153px; width: 217px; height: 73px;
    background: var(--yellow); border: 3px solid var(--navy-deep); border-radius: 10px;
    font-family: "Bebas Neue", sans-serif; color: var(--navy-deep);
    font-size: 31px; line-height: 29px; text-align: center;
    display: flex; align-items: center; justify-content: center; padding-top: 4px;
  }
  .step-body {
    position: absolute; left: 0; top: 225px; width: 213px; height: 415px;
    background: var(--white); border: 3px solid var(--navy-deep); border-top: none;
    border-radius: 0 0 12px 12px; padding: 16px 12px 0 16px;
  }
  .step-lead {
    font-weight: 700; font-size: 25px; line-height: 27px; text-align: center;
    margin-bottom: 18px;
  }
  .step-3 .step-lead { margin-top: -10px; margin-bottom: 10px; }
  .step-list { list-style: none; }
  .step-list li {
    position: relative; padding-left: 17px;
    font-weight: 500; font-size: 23px; line-height: 23px; margin-bottom: 23px;
  }
  .step-2 .step-list li { margin-bottom: 0; min-height: 46px; }
  .step-2 .step-list li.wrap { min-height: 70px; }
  .step-list li::before {
    content: ""; position: absolute; left: 0; top: 9px;
    width: 10px; height: 10px; border-radius: 50%; background: var(--yellow);
  }
  .step-3 .step-list li { margin-bottom: 24px; }
  .step-note { font-weight: 500; font-size: 23px; line-height: 25px; text-align: center; margin-top: 8px; }

  .value-art {
    position: absolute; top: 975px; width: 110px; height: 95px;
    background: #e3e9f3; border-radius: 10px;
  }
  .value {
    position: absolute; top: 1083px; width: 194px; height: 47px;
    background: var(--blue); border-radius: 12px; color: var(--white);
    font-family: "Bebas Neue", sans-serif; font-size: 44px;
    display: flex; align-items: center; justify-content: center; padding-top: 4px;
  }
  .value-arrow { position: absolute; top: 1098px; width: 38px; height: 16px; }

  .references {
    position: absolute; left: 0; top: 1148px; width: 849px; height: 52px;
    background: var(--ink); color: var(--white);
    font-family: "Barlow Condensed", sans-serif; font-weight: 500;
    font-size: 11px; line-height: 19px; padding: 6px 0 0 37px;
  }
</style>
</head>
<body>
  <svg class="backdrop" viewBox="0 0 849 1200" aria-hidden="true">
    <path d="M0 732 Q424.5 600 849 732 L849 1148 L0 1148 Z" fill="#ffffff"/>
  </svg>

  <div class="school-name"><span class="dot"></span>Calderwood High</div>

  <h1 class="title">Before you ask<br>the teacher...</h1>
  <p class="subtitle">Try these steps first!</p>

  <section class="step step-1">
    <div class="step-frame"><div class="step-icon" role="img" aria-label="Icon of a head with a brain, thinking"></div></div>
    <div class="step-number"><span>1</span></div>
    <h2 class="step-label">Think<br>first</h2>
    <div class="step-body">
      <p class="step-lead">Don't give up straight away.</p>
      <ul class="step-list">
        <li>Read the question carefully.</li>
        <li>Identify what you already know.</li>
        <li>Try a strategy you've used before.</li>
        <li>Give yourself think-ing time.</li>
      </ul>
    </div>
  </section>

  <section class="step step-2">
    <div class="step-frame"><div class="step-icon" role="img" aria-label="Icon of a checklist clipboard with a magnifying glass"></div></div>
    <div class="step-number"><span>2</span></div>
    <h2 class="step-label">Check your<br>supports</h2>
    <div class="step-body">
      <p class="step-lead">Before asking for help, check</p>
      <ul class="step-list">
        <li class="wrap">Learning goal and success criteria.</li>
        <li>Worked examples.</li>
        <li>Class notes.</li>
        <li>Classroom displays.</li>
        <li>StudyHub resources.</li>
        <li class="wrap">Task sheet and in-structions.</li>
      </ul>
    </div>
  </section>

  <section class="step step-3">
    <div class="step-frame"><div class="step-icon" role="img" aria-label="Icon of three people with a speech bubble"></div></div>
    <div class="step-number"><span>3</span></div>
    <h2 class="step-label">Ask 3 before<br>me</h2>
    <div class="step-body">
      <p class="step-lead">Ask three sources before asking the teacher:</p>
      <ul class="step-list">
        <li>A person (partner or neighbour)</li>
        <li>A place (notes, display, StudyHub)</li>
        <li>A resource (worked example, task sheet)</li>
      </ul>
      <p class="step-note">Then ask the teacher if you still need help.</p>
    </div>
  </section>

  <div class="value-art" style="left:115px" role="img" aria-label="Line illustration of two confident students"></div>
  <div class="value-art" style="left:371px" role="img" aria-label="Line illustration of students climbing a mountain"></div>
  <div class="value-art" style="left:636px" role="img" aria-label="Line illustration of students raising a flag on a summit"></div>

  <div class="value" style="left:73px">We believe</div>
  <svg class="value-arrow" style="left:282px" viewBox="0 0 38 16" aria-hidden="true">
    <path d="M2 1 L12 8 L2 15 L7 15 L17 8 L7 1 Z M18 1 L28 8 L18 15 L23 15 L33 8 L23 1 Z" fill="#1b4589"/>
  </svg>
  <div class="value" style="left:329px">We strive</div>
  <svg class="value-arrow" style="left:533px" viewBox="0 0 38 16" aria-hidden="true">
    <path d="M2 1 L12 8 L2 15 L7 15 L17 8 L7 1 Z M18 1 L28 8 L18 15 L23 15 L33 8 L23 1 Z" fill="#1b4589"/>
  </svg>
  <div class="value" style="left:594px">We achieve</div>

  <footer class="references">
    <p>Marlowe, T. (2025). "Why Students Don't Ask for Help - And How to Change That." Downloaded on 24/04/2026 from https://www.classwise.org/article/getting-students-ask-help/</p>
    <p>NERI. (2024). "Supporting Self-Regulated Learning." Downloaded on 24/04/2026 from https://www.edinsight.org/files/2024-02/supporting-self-regulated-learning.pdf</p>
  </footer>
</body>
</html>
```